VORELLO - PIZZA - RESTAURANT PIZZERIA

Flyer format:
- A5 front / back leaflet (Example attachment)
Customer logos:
- Attachment, VORELLO PIZZA logo
Address and contact to put on the flyers:
- Phone to add: (+352) 26 58 40 71 (Page 1)
- Address to be added: 27 rue des tilleuls, L-3829 Kayl, Luxembourg (Page 1)
- Website: www.vorello-example.lu (Page 1)
- Leave a space for the timetable (last page)
Flyer color:
- Preferably black background with colored customer logo
Typefaces:
- At your convenience
Descriptions:
- We would like to have a flyer to the one we have put as an example in the attachment
Important elements:
- Pizza oven on the cover page with customer logo, address and contact details
- The graphic elements must be usable and non-paying, we want a quality visual.
- Menu (attachment) The menu is in Word format, it must be laid out in a thoughtful way as on the example model.
- We need to find some pizza and/or ingredient visuals
Aspects :
- The design of the set must be elegant, sober and must contain all the information (Menu, visual of your choice, logo)

Target Market(s)

Private and professional public

Font styles to use
Serif
Sans Serif

Requirements
Must have
• Elegance, take into account the information of the comment
Nice to have
• Pizza oven, Dominant color black, Gold, red
Should not have
• poor quality visuals

```html
<!DOCTYPE html>
<html lang="fr">
<head>
<meta charset="utf-8">
<title>Vorello Pizza – Dépliant menu</title>
<link rel="stylesheet" href="https://fonts.googleapis.com/css2?family=Great+Vibes&family=Playfair+Display:wght@500;700&family=Montserrat:wght@400;600&display=swap">
<style>
  :root{
    --backdrop:#e8ab78;
    --page:#151515;
    --page-soft:#1f1d1b;
    --gold:#d9a441;
    --gold-light:#f0c56a;
    --orange:#e07a2a;
    --ink:#f2ede4;
    --ink-muted:#9d958a;
    --line:#4a4540;
  }
  *{box-sizing:border-box;margin:0;padding:0}
  html,body{width:1200px;height:800px;overflow:hidden}
  body{background:var(--backdrop);font-family:'Montserrat',sans-serif;color:var(--ink);position:relative}

  .page{position:absolute;top:140px;width:368px;height:520px;background:var(--page);overflow:hidden}
  .page--menu-left{left:28px;background:linear-gradient(160deg,var(--page-soft),var(--page))}
  .page--menu-right{left:396px;background:linear-gradient(200deg,var(--page-soft),var(--page));border-left:1px solid #2a2725}
  .page--cover{left:804px}

  .script-title{font-family:'Great Vibes',cursive;color:var(--gold-light);font-size:36px;line-height:1;font-weight:400}
  .script-title small{display:block;font-family:'Montserrat',sans-serif;font-size:7px;letter-spacing:3px;color:var(--gold);margin:-4px 0 0 26px;font-weight:600}
  .script-title--orange{color:var(--orange)}

  .menu-block{position:absolute;left:18px;width:228px}
  .menu-list{list-style:none;margin-top:8px}
  .menu-item{display:flex;align-items:baseline;font-size:7px;line-height:16px;white-space:nowrap}
  .menu-item b{font-weight:600;color:var(--ink);margin-right:4px}
  .menu-item span{color:var(--ink-muted)}
  .menu-item i{flex:1;border-bottom:1px dotted var(--line);margin:0 4px}
  .menu-item em{font-style:normal;color:var(--gold)}

  .photo{position:absolute}
  .photo--pizza-whole{right:-30px;top:44px;width:140px;height:140px;border-radius:50%;background:radial-gradient(circle at 45% 40%,#e4b15a,#c4602c 55%,#6b3a1c 75%,transparent 77%)}
  .photo--pizza-slice{right:8px;top:240px;width:96px;height:80px;border-radius:40% 50% 30% 50%;background:radial-gradient(circle at 50% 50%,#e7c064,#c05a2a 70%,#5a331a)}
  .photo--herbs{left:0;top:0;width:368px;height:40px;background:linear-gradient(90deg,rgba(70,110,40,.35),rgba(180,60,30,.25),transparent)}
  .photo--salad{right:14px;top:16px;width:70px;height:70px;border-radius:50%;background:radial-gradient(circle,#7aa44a,#3f6a2a 60%,#e9e4da 62%,#cfc7ba 72%,transparent 74%)}

  .brand-mini{position:absolute;right:92px;top:18px;font-family:'Playfair Display',serif;font-weight:700;font-size:10px;color:var(--gold);letter-spacing:1px}

  .salads{position:absolute;left:18px;top:18px;width:250px}
  .salads p{font-size:7px;line-height:13px;color:var(--ink-muted)}
  .salads p b{color:var(--ink);font-weight:600}
  .salads p em{font-style:normal;color:var(--gold)}

  .pasta{position:absolute;left:18px;top:150px;width:332px}
  .pasta-tables{display:flex;gap:18px;margin-top:8px}
  .price-table{border:1px solid var(--line);flex:1;font-size:7px}
  .price-table th{background:var(--gold);color:var(--page);font-weight:600;letter-spacing:2px;padding:3px;text-align:center}
  .price-table td{padding:3px 6px;color:var(--ink)}
  .price-table td:last-child{color:var(--gold);text-align:right}
  .price-table{border-collapse:collapse}

  .desserts{position:absolute;left:18px;top:300px;width:228px}
  .drinks{position:absolute;left:18px;top:420px;width:228px;font-size:7px;line-height:14px;color:var(--ink-muted)}
  .drinks b{color:var(--ink);font-weight:600}

  .cover-photo{position:absolute;inset:0;background:
      radial-gradient(circle at 55% 46%,#e0a24e 0,#c5542a 22%,#6a2f18 30%,transparent 34%),
      radial-gradient(ellipse at 30% 70%,#4a2e1c,transparent 40%),
      linear-gradient(180deg,#1b1a19,#0f0f0f)}
  .cover-brand{position:absolute;left:0;right:0;top:34px;text-align:center;font-family:'Playfair Display',serif;font-weight:700;color:var(--gold);font-size:40px;letter-spacing:2px;line-height:1}
  .cover-brand small{display:block;font-size:13px;letter-spacing:10px;margin-top:6px}
  .cover-contacts{position:absolute;left:14px;right:14px;bottom:16px;display:flex;flex-direction:column;gap:7px;font-size:7.5px;color:var(--ink)}
  .contact-row{display:flex;justify-content:space-between;align-items:center}
  .contact{display:flex;align-items:center;gap:5px}
  .contact svg{width:14px;height:14px;flex:none}
</style>
</head>
<body>

<section class="page page--menu-left" aria-label="Menu pizzas">
  <div class="photo photo--herbs" role="img" aria-label="Herbes fraîches et tomates cerises"></div>
  <div class="photo photo--pizza-whole" role="img" aria-label="Pizza entière découpée"></div>
  <div class="photo photo--pizza-slice" role="img" aria-label="Part de pizza"></div>

  <div class="menu-block" style="top:26px">
    <h2 class="script-title">Pizza<small>BASE TOMATE</small></h2>
    <ul class="menu-list">
      <li class="menu-item"><b>Margherita</b><span>mozzarella, basilic frais</span><i></i><em>9,50€</em></li>
      <li class="menu-item"><b>Napolitaine</b><span>anchois, câpres, olives</span><i></i><em>10,50€</em></li>
      <li class="menu-item"><b>Regina</b><span>jambon, champignons, olives</span><i></i><em>11,00€</em></li>
      <li class="menu-item"><b>Calzone</b><span>jambon, œuf, mozzarella</span><i></i><em>12,00€</em></li>
      <li class="menu-item"><b>Quatre fromages</b><span>gorgonzola, chèvre, emmental</span><i></i><em>12,50€</em></li>
      <li class="menu-item"><b>Diavola</b><span>salami piquant, poivrons</span><i></i><em>11,50€</em></li>
      <li class="menu-item"><b>Végétarienne</b><span>légumes grillés, roquette</span><i></i><em>11,50€</em></li>
      <li class="menu-item"><b>Tonno</b><span>thon, oignons rouges</span><i></i><em>11,00€</em></li>
      <li class="menu-item"><b>Capricciosa</b><span>jambon, artichauts, olives</span><i></i><em>12,00€</em></li>
      <li class="menu-item"><b>Parma</b><span>jambon cru, roquette, parmesan</span><i></i><em>13,50€</em></li>
      <li class="menu-item"><b>Hawaï</b><span>jambon, ananas, mozzarella</span><i></i><em>11,00€</em></li>
      <li class="menu-item"><b>Bolognese</b><span>viande hachée, oignons</span><i></i><em>12,00€</em></li>
    </ul>
  </div>

  <div class="menu-block" style="top:318px">
    <h2 class="script-title">Pizza<small>BASE CRÈME</small></h2>
    <ul class="menu-list">
      <li class="menu-item"><b>Bianca</b><span>crème, mozzarella, ail</span><i></i><em>10,50€</em></li>
      <li class="menu-item"><b>Carbonara</b><span>lardons, œuf, parmesan</span><i></i><em>12,00€</em></li>
      <li class="menu-item"><b>Saumon</b><span>saumon fumé, aneth</span><i></i><em>13,50€</em></li>
      <li class="menu-item"><b>Poulet</b><span>poulet, champignons, crème</span><i></i><em>12,50€</em></li>
      <li class="menu-item"><b>Chèvre miel</b><span>chèvre, miel, noix</span><i></i><em>12,50€</em></li>
      <li class="menu-item"><b>Tartufo</b><span>crème truffe, champignons</span><i></i><em>14,00€</em></li>
    </ul>
  </div>
</section>

<section class="page page--menu-right" aria-label="Menu salades, pâtes et desserts">
  <div class="brand-mini">VORELLO PIZZA</div>
  <div class="photo photo--salad" role="img" aria-label="Assiette de salade fraîche"></div>

  <div class="salads">
    <h2 class="script-title">Salads</h2>
    <p><b>César</b> — poulet, parmesan, croûtons <em>11,50€</em></p>
    <p><b>Chèvre chaud</b> — salade, toasts, miel <em>11,50€</em></p>
    <p><b>Caprese</b> — tomate, mozzarella, basilic <em>10,00€</em></p>
  </div>

  <div class="pasta">
    <h2 class="script-title">Pates</h2>
    <div class="pasta-tables">
      <table class="price-table">
        <tr><th colspan="2">SPAGHETTI</th></tr>
        <tr><td>Napolitaine</td><td>9,50€</td></tr>
        <tr><td>Bolognaise</td><td>11,00€</td></tr>
        <tr><td>Frutti di mare</td><td>14,00€</td></tr>
      </table>
      <table class="price-table">
        <tr><th colspan="2">PENNE</th></tr>
        <tr><td>Arrabbiata</td><td>10,00€</td></tr>
        <tr><td>Bolognaise</td><td>11,00€</td></tr>
        <tr><td>Carbonara</td><td>11,50€</td></tr>
      </table>
    </div>
  </div>

  <div class="desserts">
    <h2 class="script-title script-title--orange">Desserts</h2>
    <ul class="menu-list">
      <li class="menu-item"><b>Tiramisu</b><i></i><em>6,50€</em></li>
      <li class="menu-item"><b>Panna cotta</b><i></i><em>6,00€</em></li>
      <li class="menu-item"><b>Mousse chocolat</b><i></i><em>6,00€</em></li>
      <li class="menu-item"><b>Glace 2 boules</b><i></i><em>5,00€</em></li>
    </ul>
  </div>

  <div class="drinks">
    <p><b>Boissons 33 cl</b></p>
    <p>Eau plate, eau gazeuse, sodas 3,00€</p>
    <p><b>Alcools et vins</b></p>
  </div>
</section>

<section class="page page--cover" aria-label="Couverture">
  <div class="cover-photo" role="img" aria-label="Pizza sortie du four sur planche en bois, tomates et piments sur fond sombre"></div>
  <h1 class="cover-brand">VORELLO<small>PIZZA</small></h1>
  <div class="cover-contacts">
    <div class="contact-row">
      <span class="contact">
        <svg viewBox="0 0 16 16" fill="none" stroke="#d9a441" stroke-width="1.2"><circle cx="8" cy="8" r="6.5"/><path d="M1.5 8h13M8 1.5c2.2 2 2.2 11 0 13M8 1.5c-2.2 2-2.2 11 0 13"/></svg>
        (+352) 26 58 40 71
      </span>
      <span class="contact">
        <svg viewBox="0 0 16 16" fill="none" stroke="#d9a441" stroke-width="1.2"><path d="M8 14.5s-4.5-4.6-4.5-8a4.5 4.5 0 0 1 9 0c0 3.4-4.5 8-4.5 8z"/><circle cx="8" cy="6.5" r="1.6"/></svg>
        27 rue des tilleuls, L-3829 Kayl, Luxembourg
      </span>
    </div>
    <div class="contact-row">
      <span class="contact">
        <svg viewBox="0 0 16 16" fill="none" stroke="#d9a441" stroke-width="1.2"><circle cx="8" cy="8" r="6.5"/><path d="M1.5 8h13M8 1.5c2.2 2 2.2 11 0 13M8 1.5c-2.2 2-2.2 11 0 13"/></svg>
        www.vorello-example.lu
      </span>
    </div>
  </div>
</section>

</body>
</html>
```